R T Aesthetics

I would like a double sided A5 sized flyer created with a Bold, Playful, Design. The company will be providing Velunox services. We have facebook and instagam accounts set up along with a phone number, would be good to have them along the book of the back page. Simplistic design on the front, would be great to come up with a company logo that compliments the fresh look of the flyer. The back side would be for a list of services provided. I have attached a picture of an example. However other creative ideas would be of interest. Many thanks.

• It would be be good to have a box or some sort on the back page advertising "£30 off first visit" and "30% off you both when you refer a friend"
• Would be good to have a stock picture of on the front of a model of some sort etc.

```html
<!DOCTYPE html>
<html lang="en">
<head>
<meta charset="utf-8">
<title>R T Aesthetics – A5 Flyer</title>
<link href="https://fonts.googleapis.com/css2?family=Libre+Baskerville&family=Oswald:wght@400;500&family=Montserrat:ital,wght@0,500;0,600;0,700;1,800&display=swap" rel="stylesheet">
<style>
  :root {
    --canvas: #ffffff;
    --brown: #7a4518;
    --brown-dark: #5e3412;
    --gold: #a77a2c;
    --sand-light: #dcc6a4;
    --sand-dark: #bf9d70;
    --paper: #f1ede8;
    --paper-shade: #ddd6cf;
    --ink: #3a2f28;
    --rule: #b9b1a9;
    --white: #ffffff;
  }
  * { margin: 0; padding: 0; box-sizing: border-box; }
  html, body { width: 900px; height: 1200px; overflow: hidden; background: var(--canvas); }
  .canvas { position: relative; width: 900px; height: 1200px; }

  .page {
    position: absolute; top: 317px; width: 400px; height: 565px; overflow: hidden;
    box-shadow: 2px 2px 0 #9a9a9a;
  }
  .page--front { left: 35px; }
  .page--back { left: 465px; background: linear-gradient(180deg, var(--paper) 0%, var(--paper-shade) 100%); }
  .page svg { position: absolute; inset: 0; }

  .brand { position: absolute; display: flex; align-items: flex-start; gap: 7px;
    font-family: "Libre Baskerville", serif; font-weight: 400; color: var(--brown); }
  .brand__mark { width: 16px; height: 16px; background: var(--gold); margin-top: 4px; flex: none; }
  .brand__name { line-height: 1.05; }
  .brand__name span { display: block; }

  .page--front .brand { left: 30px; top: 318px; font-size: 22px; }
  .page--front .brand__mark { width: 20px; height: 20px; }
  .page--back .brand { left: 182px; top: 22px; font-size: 17px; }

  .band {
    position: absolute; left: 172px; top: 95px; width: 213px; height: 24px;
    background: var(--brown); color: var(--white);
    font-family: "Montserrat", sans-serif; font-weight: 700; font-size: 10.5px;
    display: flex; align-items: center; justify-content: center; letter-spacing: .1px;
  }

  .treatments { position: absolute; left: 172px; top: 138px; width: 213px; list-style: none; }
  .treatment { position: relative; height: 46px; display: flex; align-items: center; }
  .treatment__icon { width: 26px; height: 26px; border-radius: 6px; background: var(--brown); flex: none;
    display: flex; align-items: center; justify-content: center; }
  .treatment__icon::after { content: ""; width: 14px; height: 14px; border: 1.5px solid var(--paper); border-radius: 50%; }
  .treatment__name { margin-left: 17px; width: 48px; font-family: "Oswald", sans-serif; font-weight: 400;
    font-size: 11px; line-height: 1.35; color: var(--ink); text-transform: uppercase; }
  .treatment__rule { flex: 1; height: 1px; background: var(--rule); margin: 10px 8px 0 0; }
  .treatment__price { font-family: "Oswald", sans-serif; font-weight: 500; font-size: 20px; color: var(--ink); }
  .treatment__price sup { font-size: 9px; vertical-align: 10px; }

  .offer { position: absolute; left: 170px; width: 215px; height: 62px; display: flex; border: 1px solid var(--brown); background: var(--white); }
  .offer--first { top: 348px; }
  .offer--refer { top: 416px; }
  .offer__value { width: 76px; padding-left: 16px; display: flex; flex-direction: column; justify-content: center;
    font-family: "Montserrat", sans-serif; font-weight: 600; font-size: 19px; line-height: .98; color: var(--brown-dark); }
  .offer__value sup { font-size: 10px; vertical-align: 7px; }
  .offer__label { flex: 1; background: var(--brown); clip-path: polygon(10px 0, 100% 0, 100% 100%, 0 100%);
    display: flex; align-items: center; justify-content: center; text-align: center;
    font-family: "Montserrat", sans-serif; font-style: italic; font-weight: 800; font-size: 20px; line-height: .95; color: var(--white); }

  .contact-phone { position: absolute; right: 20px; top: 500px; display: flex; align-items: center; gap: 6px;
    font-family: "Montserrat", sans-serif; font-weight: 600; font-size: 17px; color: var(--brown); }
  .contact-phone__icon { width: 20px; height: 20px; border: 1.5px solid var(--brown); border-radius: 50%; position: relative; }
  .contact-phone__icon svg { position: absolute; left: 3px; top: 3px; }

  .social { position: absolute; left: 218px; top: 537px; width: 167px; height: 18px; border-radius: 9px;
    background: var(--brown); display: flex; align-items: center; justify-content: space-between; padding: 0 3px;
    font-family: "Montserrat", sans-serif; font-weight: 500; font-size: 11px; color: var(--white); }
  .social__dot { width: 13px; height: 13px; border-radius: 50%; background: var(--white); flex: none; }
</style>
</head>
<body>
<main class="canvas">

  <section class="page page--front" aria-label="Flyer front">
    <svg width="400" height="565" viewBox="0 0 400 565">
      <defs>
        <linearGradient id="sand" x1="0" y1="0" x2="0" y2="1">
          <stop offset="0" stop-color="var(--sand-light)"/>
          <stop offset="1" stop-color="var(--sand-dark)"/>
        </linearGradient>
        <linearGradient id="skinFront" x1="0" y1="0" x2="1" y2="1">
          <stop offset="0" stop-color="#f2d9cb"/>
          <stop offset=".55" stop-color="#f6e1d6"/>
          <stop offset="1" stop-color="#e9c3b2"/>
        </linearGradient>
      </defs>
      <rect width="400" height="565" fill="url(#sand)"/>
      <path role="img" aria-label="Portrait photograph of a model with clear skin, hand resting at her jaw"
        d="M104 0 H400 V565 H0 V510 C150 492 262 420 256 300 C250 205 150 140 104 0 Z" fill="url(#skinFront)"/>
    </svg>
    <div class="brand">
      <div class="brand__mark"></div>
      <div class="brand__name"><span>R T</span><span>Aesthetics</span></div>
    </div>
  </section>

  <section class="page page--back" aria-label="Flyer back">
    <svg width="400" height="565" viewBox="0 0 400 565">
      <defs>
        <linearGradient id="skinBack" x1="0" y1="0" x2="1" y2="0">
          <stop offset="0" stop-color="#ecd3c6"/>
          <stop offset=".75" stop-color="#f3e2d9"/>
          <stop offset="1" stop-color="#f1ede8" stop-opacity="0"/>
        </linearGradient>
      </defs>
      <rect role="img" aria-label="Portrait photograph of a model looking over her bare shoulder" x="0" y="0" width="200" height="565" fill="url(#skinBack)"/>
    </svg>

    <div class="brand">
      <div class="brand__mark"></div>
      <div class="brand__name"><span>R T</span><span>Aesthetics</span></div>
    </div>

    <div class="band">OUR TREATMENTS CAN TARGET</div>

    <ul class="treatments">
      <li class="treatment"><span class="treatment__icon"></span><span class="treatment__name">Forehead lines</span><span class="treatment__rule"></span><span class="treatment__price"><sup>$</sup>90.<sup>00</sup></span></li>
      <li class="treatment"><span class="treatment__icon"></span><span class="treatment__name">Frown lines</span><span class="treatment__rule"></span><span class="treatment__price"><sup>$</sup>80.<sup>00</sup></span></li>
      <li class="treatment"><span class="treatment__icon"></span><span class="treatment__name">Bunny lines</span><span class="treatment__rule"></span><span class="treatment__price"><sup>$</sup>70.<sup>00</sup></span></li>
      <li class="treatment"><span class="treatment__icon"></span><span class="treatment__name">Crows feet</span><span class="treatment__rule"></span><span class="treatment__price"><sup>$</sup>60.<sup>00</sup></span></li>
    </ul>

    <div class="offer offer--first">
      <div class="offer__value"><span><sup>£</sup>30</span><span>Off</span></div>
      <div class="offer__label">FIRST<br>VISIT</div>
    </div>
    <div class="offer offer--refer">
      <div class="offer__value"><span>30<sup>%</sup></span><span>Off</span></div>
      <div class="offer__label">REFER A<br>FRIEND</div>
    </div>

    <div class="contact-phone">
      <span class="contact-phone__icon">
        <svg width="12" height="12" viewBox="0 0 24 24"><path d="M6.6 10.8a15 15 0 0 0 6.6 6.6l2.2-2.2c.3-.3.7-.4 1-.2 1.1.4 2.3.6 3.6.6.6 0 1 .4 1 1V20c0 .6-.4 1-1 1A17 17 0 0 1 3 4c0-.6.4-1 1-1h3.5c.6 0 1 .4 1 1 0 1.3.2 2.5.6 3.6.1.3 0 .7-.2 1l-2.3 2.2z" fill="var(--brown)"/></svg>
      </span>
      <span>555-014-2368</span>
    </div>

    <div class="social">
      <span class="social__dot"></span>
      <span>Rt aesthetics</span>
      <span class="social__dot"></span>
    </div>
  </section>

</main>
</body>
</html>
```